依頼詳細
12月1日の開催である為、クリスマスをイメージした上品なデザインで、配色はゴールドや赤色を希望しています。ターゲットは50代~70代のハイクラスな女性です。

記載項目
添付資料の通り、ご記載下さいませ。
サイズ
A4
ページ数
片面
希望イメージ
シンプル 複雑
単色 カラフル
暗い 明るい
日常 高級
遊び心 厳粛
未来的 伝統的
女性的 男性的
希望する色
赤系、ゴールドを思わせる色調を希望。
納品ファイル
• 高解像度JPG (.jpg)
• イラストレーター形式 (.ai)
補足説明
【チラシを御考案下さる皆様へ】

いつも素敵なデザインをご提案下さいまして、誠にありがとうございます。
この度は、第6回目となります「ひだまりチェロ・フェスティバルin岡山」のチラシデザインをお願いしたいと存じます。
出演者の皆様は、1分15秒のステージに向けて一生懸命に練習をされていますので、このチラシで出演者様もご来場者様もワクワクしていただけますと幸いに存じます。
どうぞ宜しくお願い申し上げます。

by.日本ひだまりチェロ連盟
追記:添付ファイルをご参照下さいませ。
大変素敵な御提案を下さり、誠にありがとうございます。
既に数点、感謝しつつ拝見しております。

背景についてですが、
必ずしもグランドピアノが必要であるとは思っておりません。
音楽に拘らず、クリスマスの雰囲気でワクワク上品な雰囲気であれば、
何ら問題ございません。

どうぞ宜しくお願い申し上げます。
【デザインをご考案頂きました皆様へ】

この度は、「中高年ピアノフェスティバル・チラシ」のデザインをご考案頂きまして、誠にありがとうございました。

本当に素晴らしい作品ばかりで、胸がジーンとしてまいります。

心から感謝申し上げます。

現在ご提案頂きました作品一点一点を、関係者と共に選定中でございます。

何卒宜しくお願い申し上げます。

取り急ぎ御礼まで。

日本ひだまりチェロ連盟
■ 選んだ理由

この作品は、落ち着いた赤色の中にも、華やかさがある大人のクリスマスを感じさせるデザインで、ピアノ講師陣の一番人気の作品でした。全体のイメージが何かが起こりそうな楽しい予感を感じ、文字も大変読みやすいデザインです。この様なチラシを皆様に配りすることが出来、大変嬉しく思っております。改めまして御礼申し上げます。

■ 提案者全員のお礼・コメント

この度は、「中高年ピアノフェスティバル・チラシ」のデザインをご考案下さいまして、誠にありがとうございます。デザイナー様のお一人お一人の熱い想いのこもった数々の作品に、本当に胸が一杯でございます。クリスマスのイメージはもちろんですが、60代から70代の年齢に合わせて読みやすくなさって下さったり、書体の工夫。。と細部にわたるご配慮、改めまして心より御礼申し上げます。今後もイベントに合わせてコンペ方式でデザインのご提案を依頼させて頂くことがございますので、引き続き宜しくお願い申し上げます!

```html
<!DOCTYPE html>
<html lang="ja">
<head>
<meta charset="utf-8">
<title>ひだまりチェロ・フェスティバルin岡山</title>
<link rel="stylesheet" href="https://fonts.googleapis.com/css2?family=Noto+Sans+JP:wght@400;700;900&family=Shippori+Mincho:wght@600;800&display=swap">
<style>
:root{
  --wine:#6e0c12;
  --wine-deep:#4a060a;
  --red:#b3121c;
  --gold:#d6b15a;
  --gold-light:#f3dc9a;
  --cream:#fff8e8;
  --ink:#2a1a14;
  --line:#9a7a6a;
  --white:#ffffff;
}
*{box-sizing:border-box;margin:0;padding:0}
html,body{width:849px;height:1200px;overflow:hidden;background:var(--white)}
body{font-family:"Noto Sans JP",sans-serif;color:var(--ink)}
.flyer{position:relative;width:849px;height:1200px;overflow:hidden}

.stage{position:absolute;left:0;top:0;width:849px;height:852px;
  background:radial-gradient(ellipse at 55% 35%,#a0141c 0%,var(--wine) 55%,var(--wine-deep) 100%)}
.art-keys{position:absolute;left:0;top:0;width:400px;height:175px;
  background:linear-gradient(160deg,#1a1010 0%,#3b1a1a 40%,#efe6dc 70%,rgba(110,12,18,0) 100%)}
.art-sleigh{position:absolute;right:20px;top:20px;width:210px;height:70px;
  background:linear-gradient(90deg,rgba(243,220,154,0) 0%,rgba(243,220,154,.45) 100%);border-radius:40px}
.art-glass{position:absolute;left:560px;top:190px;width:289px;height:330px;
  background:radial-gradient(ellipse at 45% 35%,#f7e7b8 0%,#d9b46a 30%,rgba(150,70,30,.5) 60%,rgba(110,12,18,0) 80%)}

.lead{position:absolute;left:0;width:849px;top:16px;text-align:center;
  font-family:"Shippori Mincho",serif;font-weight:800;font-size:22px;color:var(--gold-light);letter-spacing:2px}

.badge{position:absolute;left:22px;top:200px;width:118px;height:118px;border-radius:50%;
  background:var(--white);border:4px solid var(--gold);display:flex;flex-direction:column;
  align-items:center;justify-content:center;color:var(--red);font-weight:900;line-height:1.2;text-align:center}
.badge .time{font-size:17px}
.badge .word{font-family:"Shippori Mincho",serif;font-size:27px}

.title{position:absolute;left:150px;top:160px;width:560px;text-align:center;white-space:nowrap;
  font-family:"Shippori Mincho",serif;font-weight:800;color:var(--gold-light);line-height:1.15}
.title .name{display:block;font-size:36px}
.title .event{display:block;font-size:44px;color:var(--gold)}
.title .event small{font-size:28px;color:var(--gold-light)}
.catch{position:absolute;left:150px;top:285px;width:560px;text-align:center;white-space:nowrap;
  font-family:"Shippori Mincho",serif;font-weight:800;color:var(--white)}
.catch .big{font-size:26px;display:block}
.catch .sub{font-size:15px;color:var(--gold-light);display:block;margin-top:6px}

.date{position:absolute;left:80px;top:400px;display:flex;align-items:flex-end;gap:10px;color:var(--white);white-space:nowrap}
.date .year{font-size:18px;font-weight:700;color:var(--gold-light);margin-bottom:10px}
.date .label{font-size:30px;font-weight:900}
.date .day{font-family:"Shippori Mincho",serif;font-weight:800;font-size:64px;color:var(--gold-light);line-height:1}
.date .unit{font-size:30px;font-weight:900}
.date .dow{display:inline-block;width:34px;height:34px;border-radius:50%;background:var(--white);
  color:var(--red);font-size:20px;font-weight:900;text-align:center;line-height:34px;margin-bottom:8px}
.hours{position:absolute;left:545px;top:414px;border-left:2px solid var(--gold);padding-left:10px;
  color:var(--white);font-size:15px;font-weight:700;line-height:1.6;white-space:nowrap}
.venue{position:absolute;left:80px;top:490px;color:var(--white);font-size:24px;font-weight:900;white-space:nowrap}
.venue span{color:var(--gold-light)}

.cats{position:absolute;left:22px;top:538px;width:805px;display:flex;gap:14px}
.cat{background:var(--cream);border:2px solid var(--gold);border-radius:6px;padding:8px 10px;color:var(--ink)}
.cat h3{font-size:13.5px;font-weight:900;color:var(--red);border-bottom:1px solid var(--gold);padding-bottom:4px;margin-bottom:6px;white-space:nowrap}
.cat h3 b{font-size:18px}
.cat p{font-size:13px;font-weight:700;line-height:1.6;white-space:nowrap}
.tag{display:inline-block;background:var(--red);color:var(--white);font-size:11px;padding:0 5px;border-radius:3px;margin-right:4px}
.cat-grade{width:268px}
.cat-free{width:245px}
.cat-group{width:264px}
.pricelist{display:grid;grid-template-columns:auto auto;column-gap:12px;font-size:13px;font-weight:700;line-height:1.55}
.pricelist dd{text-align:right}
.note{font-size:11px;color:var(--line);margin-top:4px}

.info{position:absolute;left:22px;top:690px;width:478px;color:var(--white);font-size:11px;line-height:1.55}
.info strong{color:var(--gold-light)}
.bank{position:absolute;left:510px;top:690px;width:317px;background:rgba(255,255,255,.08);
  border:1px solid var(--gold);padding:6px 10px;color:var(--white);font-size:12px;line-height:1.6}
.bank strong{color:var(--gold-light)}
.org{position:absolute;left:160px;top:786px;display:flex;align-items:center;gap:10px;color:var(--white)}
.org .dot{width:34px;height:34px;border-radius:50%;background:var(--gold)}
.org .sm{font-size:12px;display:block;line-height:1.3}
.org .nm{font-size:24px;font-weight:900;display:block;line-height:1.1}
.org .tg{font-size:11px;display:block;color:var(--gold-light);line-height:1.4}

.form{position:absolute;left:22px;top:858px;width:805px}
.form-head{display:flex;justify-content:space-between;align-items:flex-end;border-bottom:2px solid var(--red);padding-bottom:3px;margin-bottom:6px}
.form-head h2{font-size:17px;font-weight:900;color:var(--red)}
.form-head span{font-size:11px;color:var(--line)}
table{width:100%;border-collapse:collapse;font-size:12px;margin-bottom:8px}
th,td{border:1px solid var(--line);padding:3px 6px;text-align:left;vertical-align:middle}
th{background:#f6ece6;font-weight:700;white-space:nowrap;width:70px}
.r28 td,.r28 th{height:28px}
.r34 td,.r34 th{height:34px}
.box{display:inline-block;width:10px;height:10px;border:1px solid var(--ink);margin-right:4px;vertical-align:-1px}
.foot{font-size:10.5px;color:var(--line);text-align:right}
</style>
</head>
<body>
<div class="flyer">
  <section class="stage">
    <div class="art-keys" role="img" aria-label="グランドピアノの鍵盤のイラスト"></div>
    <div class="art-sleigh" role="img" aria-label="夜空を駆けるサンタのそりのシルエット"></div>
    <div class="art-glass" role="img" aria-label="泡立つシャンパングラスの写真"></div>

    <p class="lead">趣味で楽しみたい演奏者大募集!</p>

    <div class="badge"><span class="time">1分15秒の</span><span class="word">花舞台</span></div>

    <h1 class="title">
      <span class="name">「ひだまりチェロ・</span>
      <span class="event">フェスティバル<small>in</small>岡山」</span>
    </h1>
    <p class="catch">
      <span class="big">〜ここまで弾けた!その喜びを〜</span>
      <span class="sub">貴方の自信を持ってチャレンジしてみませんか</span>
    </p>

    <div class="date">
      <span class="year">2015年</span>
      <span class="label">日時：</span>
      <span class="day">12</span><span class="unit">月</span>
      <span class="day">1</span><span class="unit">日</span>
      <span class="dow">火</span>
    </div>
    <div class="hours">開場 13:30<br>開演 14:00</div>
    <p class="venue">会場：<span>岡山中央文化会館 ひかりホール</span></p>

    <div class="cats">
      <div class="cat cat-grade">
        <h3>ひだまりチェロ グレード認定<b>47</b>部門</h3>
        <p><span class="tag">演奏時間</span>1分15秒以内</p>
        <dl class="pricelist">
          <dt>参加費 課題1つ選択</dt><dd>5,940円</dd>
          <dt>　　　 課題2つ選択</dt><dd>6,480円</dd>
          <dt>　　　 課題3つ選択</dt><dd>7,020円</dd>
        </dl>
      </div>
      <div class="cat cat-free">
        <h3>自由演奏部門</h3>
        <p><span class="tag">演奏時間</span>1分15秒以内</p>
        <p><span class="tag">参加費</span>5,400円</p>
        <p class="note">※曲目は自由にお選びいただけます</p>
      </div>
      <div class="cat cat-group">
        <h3>グループ演奏部門</h3>
        <p><span class="tag">演奏時間</span>2名で演奏 2分15秒以内</p>
        <p>　　　　　3名以上 3分15秒以内</p>
        <p><span class="tag">参加費</span>1名あたり 3,780円</p>
      </div>
    </div>

    <div class="info">
      <strong>■申し込み方法</strong> 下記申込書に必要事項をご記入の上、郵送またはFAXにてお送り下さい。参加費は指定口座へお振込み下さい。<br>
      <strong>■お問合せ</strong> 〒530-0099 大阪府大阪市北区みなみ町3-8 梅田みなみビル7階<br>
      日本ひだまりチェロ連盟 事務局　TEL 06-0000-1234　FAX 06-0000-1235<br>
      E-mail info@hidamari-cello.example
    </div>
    <div class="bank">
      <strong>【お振込先】</strong><br>
      みどり中央銀行 岡山支店<br>
      普通 0172345　日本ひだまりチェロ連盟
    </div>

    <div class="org">
      <span class="dot"></span>
      <span>
        <span class="sm">一般社団法人</span>
        <span class="nm">日本ひだまりチェロ連盟</span>
        <span class="tg">「気軽・身近・楽しい」の生涯教育</span>
      </span>
    </div>
  </section>

  <section class="form">
    <div class="form-head">
      <h2>参加申込書／10月2日(金)締切</h2>
      <span>(きりとらずにお送り下さい)</span>
    </div>
    <table>
      <tr class="r28"><th>ふりがな</th><td></td><th>ご年齢</th><td style="width:80px;text-align:right">歳</td><th>性別</th><td style="width:80px">男・女</td></tr>
      <tr class="r34"><th>お名前</th><td colspan="5"></td></tr>
      <tr class="r34"><th>ご住所</th><td colspan="5">〒</td></tr>
      <tr class="r28"><th>お電話</th><td colspan="3"></td><th>FAX</th><td></td></tr>
    </table>
    <table>
      <tr class="r28"><th>参加部門</th><th>曲　名</th><th>作曲者名</th><th>演奏時間</th><th>受付番号</th></tr>
      <tr class="r28"><td><span class="box"></span>グレード認定47部門</td><td></td><td></td><td>分　秒</td><td></td></tr>
      <tr class="r28"><td><span class="box"></span>自由演奏部門</td><td></td><td></td><td>分　秒</td><td></td></tr>
      <tr class="r28"><td><span class="box"></span>グループ演奏部門</td><td></td><td></td><td>分　秒</td><td></td></tr>
    </table>
    <p class="foot">ご記入いただいた個人情報は本イベントの運営以外には使用いたしません。</p>
  </section>
</div>
</body>
</html>
```